Raw Food & Health Coach Needs a Clutch Coupon

I need a clutch coupon for a raw food & health coaching business based in Washington, DC called Maren Okafor, LLC. I help ladies and gents on the go who want to support their bodies to stay healthy or prevent/correct disease so they can live extraordinary lives while deeply serving the world. My services include individual coaching, (online) group coaching, and corporate wellness coaching.

I would like to create a clutch coupon to give to referral partners who in turn will give them to their clients. So far I have two referral partners in mind: Tobias Venn Salon & Spa; and Colon Hydrotherapist Greta Mulvane.

Tobias Venn Salon & Spa will be having an event on Thursday, September 12, 2013, during which time their clients who get a hair cut will receive a complimentary Plumetra (hair) Treatment & a complimentary Radiant Roots Forward Blueprint Session with me.

I would like to see designs that use 2-4 colors, including a bit of green. The final design should communicate beauty/health from the inside out and boundless energy to enjoy an extraordinary life. It should be natural yet elegant/classy.

Designers are currently working on my business logo. The logo design project has not yet been completed. Once it completes, I will send the logo design to you and request that you incorporate the logo into your coupon design.

IMPORTANT: I need to select a winning design on Wed, Sept 11, 2013, and get the source files from the designer within 24 hours (before Thursday, Sept 12 MORNING); so that I have time to adjust any text and take it to the printer in order to distribute the coupon later that afternoon. I will need the source files urgently (within the next 24 hours).

Then after the event the designer will make the changes on the design for me incorporating my logo for use with multiple referral partners. I will approve the Payment when I have finalized the design

To repeat, I must have the winning design on September 11 (or Sept 12 morning at the latest).

IMPORTANT: Refer to uploaded Referral Partner Clutch Coupon SAMPLE to give you an idea of the layout I'd like, but PLEASE don't let it stifle YOUR creativity.
Updates

The focus should be on the Free Radiant Roots Forward Blueprint Session, not on me.

 

I think I’d prefer a white background and black text, unless you can convince me otherwise by showing me a beautiful design.

 

Ensure there is space between paragraphs.

 

Somehow differentiate my free gift (Vital Shield Starter Kit), phone and URL at the bottom on the back. While it would be nice to include my free gift, I may have to leave out if it won’t fit on the coupon.

Reason: Not completely satisfied yet and open to more designs. Maren

Reason: Need more time and would like to see more designs.

Target Market(s)

The audience is busy, heart-centered/socially responsible professional men and women on the go who hardly have time for self-care, but who will pay for holistic services (alternative therapies) to enhance their beauty/health so that they can perform their best while deeply serving the world without getting sick or having to endure toxic therapies like surgery, chemotherapy, radiation, and pills.

Industry/Entity Type

Printer

Requirements
Must have
• 2-4 colors, including a little green

Dimensions: approx. 2.25 inches x 5.25 inches.

Text from the uploaded file. Note: I'm not sure if all the text I've provided will fit nicely on the back of the coupon. If no then please increase the dimensions as little as possible.

The front of the coupon designed horizontally, and the back designed vertically.
Nice to have
• I'm open to your using illustrations or photos of the raw food and/or lifestyle tools that I use with clients in my business, such as green juice, (leafy) green veggies, cucumbers, lemons, berries, green smoothies, superfoods, movement/exercise, self-care...

I also like the idea of including a face in the design. When I’ve surveyed in the past people have related better to a face than just to a bowl of veggies or fruit.
Should not have
• the colors orange or red, or florescent colors.

```html
<!DOCTYPE html>
<html lang="en">
<head>
<meta charset="utf-8">
<title>Maren Okafor – Clutch Coupon</title>
<link rel="stylesheet" href="https://fonts.googleapis.com/css2?family=Arimo:wght@400;700&family=Josefin+Sans:wght@300&family=Ubuntu:wght@400;500;700&display=swap">
<style>
  :root {
    --page: #e8e5e0;
    --card: #ffffff;
    --ink: #1a1a1a;
    --green: #21a84a;
    --leaf: #8cc63f;
    --purple: #7a4f96;
    --rule: #9b86b5;
  }
  * { box-sizing: border-box; margin: 0; padding: 0; }
  html, body { width: 1200px; height: 748px; overflow: hidden; }
  body { background: var(--page); position: relative; color: var(--ink); font-family: "Ubuntu", sans-serif; }

  .card { position: absolute; background: var(--card); box-shadow: 0 2px 8px rgba(0,0,0,.18); overflow: hidden; }

  /* Front */
  .front { left: 108px; top: 235px; width: 652px; height: 278px; }
  .front .name { position: absolute; left: 20px; top: 18px; font-family: "Josefin Sans", sans-serif; font-weight: 300; font-size: 36px; letter-spacing: .5px; }
  .front .role { position: absolute; left: 20px; top: 62px; font-family: "Arimo", sans-serif; font-size: 18px; }
  .front .ornament { position: absolute; left: 58px; top: 98px; width: 140px; height: 112px; border-radius: 40%; background: radial-gradient(circle at 40% 45%, var(--purple) 0%, var(--leaf) 45%, #c9e59a 70%, rgba(255,255,255,0) 72%); }
  .front .divider { position: absolute; left: 264px; top: 18px; width: 2px; height: 188px; background: var(--rule); }
  .front .offer { position: absolute; left: 272px; top: 22px; width: 376px; text-align: center; font-size: 17px; line-height: 1.3; }
  .front .offer p + p { margin-top: 18px; }
  .front .band { position: absolute; left: 0; right: 0; top: 234px; height: 30px; background: var(--green); color: #fff; font-family: "Arimo", sans-serif; font-size: 19px; line-height: 30px; text-align: center; }

  /* Back */
  .back { left: 813px; top: 49px; width: 279px; height: 651px; }
  .back .title { position: absolute; left: 16px; top: 16px; font-family: "Arimo", sans-serif; font-weight: 700; font-size: 44px; }
  .back .ornament { position: absolute; left: 168px; top: 8px; width: 96px; height: 78px; border-radius: 45%; background: radial-gradient(circle at 50% 50%, var(--purple) 0%, var(--leaf) 45%, #d4ebab 70%, rgba(255,255,255,0) 72%); }
  .back .faq { position: absolute; left: 10px; right: 10px; top: 92px; text-align: center; }
  .back .faq h2 { font-size: 16px; font-weight: 700; line-height: 1.2; }
  .back .faq p { font-size: 11.3px; line-height: 1.3; margin-top: 2px; }
  .back .faq section + section { margin-top: 18px; }
  .back .rule { position: absolute; left: 16px; right: 16px; top: 506px; height: 2px; background: var(--rule); }
  .back .portrait { position: absolute; left: 18px; top: 524px; width: 84px; height: 86px; background: linear-gradient(160deg, #6b4a35, #c79b7d 55%, #3f2a1e); border: 3px solid #fff; box-shadow: 0 1px 4px rgba(0,0,0,.35); }
  .back .cta { position: absolute; left: 106px; top: 522px; width: 168px; text-align: center; font-family: "Arimo", sans-serif; font-size: 16px; line-height: 1.25; }
  .back .cta strong { display: block; margin-top: 8px; font-size: 16px; }
  .back .band { position: absolute; left: 0; right: 0; top: 618px; height: 33px; background: var(--green); color: #fff; font-family: "Arimo", sans-serif; font-weight: 700; font-size: 16px; line-height: 33px; text-align: center; }
</style>
</head>
<body>
  <article class="card front">
    <h1 class="name">Maren Okafor</h1>
    <div class="role">Raw Food &amp; Health Coach</div>
    <div class="ornament" role="img" aria-label="Green and purple floral swirl ornament"></div>
    <div class="divider"></div>
    <div class="offer">
      <p>Free Radiant Roots Forward Blueprint Session with <strong>Certified Raw Food &amp; Health Coach</strong>, Maren Okafor.</p>
      <p>30 minutes, focused entirely on you <strong>(a $50 value, free).</strong></p>
      <p>Compliments of <strong>Tobias Venn Salon &amp; Spa.</strong></p>
    </div>
    <div class="band">To schedule your appointment, simply go to: <strong>http://bit.ly/RRfwd</strong></div>
  </article>

  <article class="card back">
    <h2 class="title">Q. &amp; A.</h2>
    <div class="ornament" role="img" aria-label="Green and purple floral swirl ornament"></div>
    <div class="faq">
      <section>
        <h2>What is Raw Food &amp; Health Coaching?</h2>
        <p>Raw food coaching helps you go or stay raw to the level that you truly desire. Health coaching helps you connect the dots between what you eat and how you feel. You’ll know how to detoxify and oxygenate your body, alkalize your pH, and delight in what you eat like never before – without restriction.</p>
      </section>
      <section>
        <h2>Who benefits from this work?</h2>
        <p>Smart, service-oriented ladies and gents on the go who want to enable their bodies to prevent/correct disease and create energy so they can live extraordinary lives without crashing, getting sick or neglecting their own health.</p>
      </section>
      <section>
        <h2>What happens in the initial consultation?</h2>
        <p>This 30 minute phone call is a time to discuss your unique health challenge(s) and desires. I guarantee you’ll walk away with at least 1 aha about why you’re stuck and more clarity about what it’ll take to put you on the fast track to where you want to go.</p>
      </section>
    </div>
    <div class="rule"></div>
    <div class="portrait" role="img" aria-label="Portrait photo of the coach"></div>
    <div class="cta">To schedule your appointment, simply go to:<strong>http://bit.ly/RRfwd</strong></div>
    <div class="band">202-555-0147, marenokafor.com</div>
  </article>
</body>
</html>
```